Blog Banner Design Project: Harbour Lantern Guides

Looking for a new banner for my blog " Owen Pelsworth's Harbour Lantern Guides" at http://www.harbourlanternguides-demo.net - and once design agreed also want an updated album art for the podcast that goes along with the site.
For more about the blog and what it is about:
http://www.harbourlanternguides-demo.net/about
Harbour Lantern Guides is a Luxury Travel Blog And Podcast that provides inspiration, advice and tips about luxurious travel experiences, including destinations, transportation, accommodation, and journeys, that travellers can read, listen to or watch.
Objective of the new design
(1) retain the colour scheme ideally to retain the brand identity, as have been using these colours since 2005.
(2) introduce more of my personality and make it more visually and overt that it is "Owen Pelsworth's Harbour Lantern Guides", so possibly introducing my image into the blog banner so visitors are clear and more aware of the person behind the brand.
(3) needs to have an up-market, luxury but modern feel.
(4) if possible reflect the focus on the content (destinations, transportation, accommodation, attractions and journeys) - but this maybe best left to just words as want the design to be bold and more of the branding and personality.
Ideal wording
Smallish: Owen Pelsworth's
Main wording: Harbour Lantern Guides
Sub-title/ small: luxurious destinations, transportation, accommodation and journeys.
I have a poll running with readers of my blog to rate the designs to help me to chose the final route, and so there is no need to submit any more designs. I will make the decision once the poll closes on the weekend.

```html
<!DOCTYPE html>
<html lang="en">
<head>
<meta charset="utf-8">
<title>Owen Pelsworth's Harbour Lantern Guides – Blog Banner</title>
<link rel="stylesheet" href="https://fonts.googleapis.com/css2?family=Arimo:wght@400;700&family=Questrial&display=swap">
<style>
  :root {
    --amber: #ffab00;
    --lavender: #b9a6cf;
    --lavender-pale: #e4dcef;
    --plum: #8c1c8c;
    --ink: #000000;
    --slate: #6a6a6a;
    --white: #ffffff;
    --photo-dark: #3a3a44;
    --photo-light: #9a8fa6;
  }
  html, body {
    margin: 0;
    padding: 0;
    overflow: hidden;
    background: var(--white);
  }
  .banner {
    position: relative;
    width: 1200px;
    height: 172px;
    overflow: hidden;
    background: var(--amber);
  }
  .banner__backdrop {
    position: absolute;
    inset: 0;
  }
  .banner__text {
    position: absolute;
    left: 0;
    margin: 0;
    color: var(--white);
    white-space: nowrap;
  }
  .banner__owner {
    top: 13px;
    left: 376px;
    font-family: "Arimo", Arial, sans-serif;
    font-weight: 400;
    font-size: 23px;
    line-height: 30px;
    letter-spacing: 0.2px;
  }
  .banner__title {
    top: 47px;
    left: 376px;
    font-family: "Arimo", Arial, sans-serif;
    font-weight: 700;
    font-size: 35px;
    line-height: 42px;
  }
  .banner__tagline {
    top: 96px;
    left: 360px;
    font-family: "Questrial", "Century Gothic", sans-serif;
    font-weight: 400;
    font-size: 20px;
    line-height: 30px;
    color: #f2f2f2;
  }
</style>
</head>
<body>
  <header class="banner">
    <svg class="banner__backdrop" width="1200" height="172" viewBox="0 0 1200 172" aria-hidden="false">
      <defs>
        <linearGradient id="palm-wash" x1="0" y1="0" x2="1" y2="0.4">
          <stop offset="0" stop-color="var(--lavender-pale)"/>
          <stop offset="0.55" stop-color="var(--lavender)"/>
          <stop offset="1" stop-color="var(--lavender)" stop-opacity="0"/>
        </linearGradient>
        <linearGradient id="portrait-tone" x1="0" y1="0" x2="0" y2="1">
          <stop offset="0" stop-color="var(--photo-light)"/>
          <stop offset="1" stop-color="var(--photo-dark)"/>
        </linearGradient>
      </defs>

      <rect class="backdrop__amber" width="1200" height="172" fill="var(--amber)"/>
      <polygon class="backdrop__palm-wash" points="0,0 470,0 380,172 0,172" fill="url(#palm-wash)"
               role="img" aria-label="Soft lavender palm fronds decoration"/>

      <polygon class="bar bar--owner" points="349,14 762,14 762,46 347,46" fill="var(--plum)"/>
      <polygon class="bar bar--title" points="334,46 1200,46 1200,93 331,93" fill="var(--ink)"/>
      <polygon class="bar bar--tagline" points="331,95 1181,95 1181,127 329,127" fill="var(--slate)"/>

      <path class="portrait" d="M196,172 L196,120 Q200,96 224,86 L232,20 Q258,0 290,20 L300,86 Q326,96 332,120 L334,172 Z"
            fill="url(#portrait-tone)" role="img" aria-label="Portrait photo of Owen Pelsworth in a hoodie"/>
    </svg>

    <p class="banner__text banner__owner">Owen Pelsworth’s</p>
    <h1 class="banner__text banner__title">Harbour Lantern Guides</h1>
    <p class="banner__text banner__tagline">Luxurious Destinations, Transportation, Accommodation and Journeys</p>
  </header>
</body>
</html>
```